QALD Digital Guard Model R3 2 in 1 Data Protection & Rules

Book Cover Name:
QALD Digital Guard Model R3
2-in-1 Data Protection & Rules

Summary:
I need a cover for a book. This is actually two books combine. A bundle of 2 computer security books. I have attached the designs from the old books.

```html
<!DOCTYPE html>
<html lang="en">
<head>
<meta charset="utf-8">
<title>QALD Digital Guard Model R3 — 2-in-1 Data Protection &amp; Rules</title>
<link rel="stylesheet" href="https://fonts.googleapis.com/css2?family=Bebas+Neue&display=swap">
<style>
  :root {
    --navy-top: #060b20;
    --navy-bottom: #050a33;
    --gold-top: #e9b604;
    --gold-bottom: #ebd006;
    --ink: #05050f;
    --white: #ffffff;
    --glow-core: #2a55ff;
    --glow-edge: rgba(20, 40, 180, 0);
  }
  * { margin: 0; padding: 0; box-sizing: border-box; }
  html, body { width: 750px; height: 1200px; overflow: hidden; background: var(--navy-top); }
  .cover {
    position: relative;
    width: 750px;
    height: 1200px;
    overflow: hidden;
    background: linear-gradient(180deg, var(--navy-top) 0%, var(--navy-top) 45%, var(--navy-bottom) 100%);
    font-family: "Bebas Neue", "Oswald", sans-serif;
    text-transform: uppercase;
  }
  .series-line {
    position: absolute;
    top: 35px; left: 0; width: 100%;
    text-align: center;
    font-size: 57px;
    line-height: 1;
    letter-spacing: 1px;
    color: var(--white);
  }
  .series-name {
    position: absolute;
    top: 96px; left: 0; width: 100%;
    text-align: center;
    font-size: 237px;
    line-height: 1;
    letter-spacing: 2px;
    background: linear-gradient(180deg, var(--gold-top) 30%, var(--gold-bottom) 90%);
    -webkit-background-clip: text;
    background-clip: text;
    color: transparent;
  }
  .title-band {
    position: absolute;
    top: 327px; left: 0;
    width: 100%; height: 114px;
    display: flex; align-items: center; justify-content: center;
    background: linear-gradient(180deg, var(--gold-top) 0%, var(--gold-bottom) 85%);
  }
  .title-band span {
    font-size: 103px;
    line-height: 1;
    padding-top: 8px;
    color: var(--ink);
    letter-spacing: 1px;
  }
  .title-sub {
    position: absolute;
    top: 452px; left: 0; width: 100%;
    text-align: center;
    font-size: 128px;
    line-height: 1;
    letter-spacing: 3px;
    background: linear-gradient(180deg, var(--gold-top) 20%, var(--gold-bottom) 90%);
    -webkit-background-clip: text;
    background-clip: text;
    color: transparent;
  }
  .edition-badge {
    position: absolute;
    top: 591px; left: 314px;
    width: 148px; height: 148px;
    border-radius: 50%;
    background: linear-gradient(180deg, var(--gold-top) 0%, var(--gold-bottom) 100%);
    display: flex; align-items: center; justify-content: center;
  }
  .edition-badge span {
    font-size: 124px;
    line-height: 1;
    padding-top: 10px;
    color: var(--ink);
  }
  .lock-art {
    position: absolute;
    top: 760px; left: 175px;
    width: 430px; height: 300px;
    background: radial-gradient(ellipse 45% 50% at 50% 50%, var(--glow-core) 0%, rgba(30, 60, 230, 0.55) 45%, var(--glow-edge) 100%);
  }
  .author {
    position: absolute;
    top: 1106px; left: 0; width: 100%;
    text-align: center;
    font-size: 78px;
    line-height: 1;
    letter-spacing: 1px;
    color: var(--white);
  }
</style>
</head>
<body>
  <main class="cover">
    <p class="series-line">2-in-1 Data Protection &amp; Rules</p>
    <h1 class="series-name">QALD</h1>
    <div class="title-band"><span>Digital Guard</span></div>
    <p class="title-sub">Model</p>
    <div class="edition-badge"><span>R3</span></div>
    <div class="lock-art" role="img" aria-label="Glowing blue digital padlock made of circuit dots over a dark data grid"></div>
    <p class="author">Author Name</p>
  </main>
</body>
</html>
```